Selka Marven Photography Business Card

I need a new business card/ possibly design to use for other marking materials ... I have included my logo below in a few different colors, but can also provide the logo in additional colors and sizes. I would love a card the expresses clean, simple and classy.

Target Market(s)

Portrait photography clients, child photography clients

Industry/Entity Type

Photographer

Contact Information for Business Card

Selka Marven Photography, Glenmoor MA, www.selkamarvenphotography-demo.com
T. 555-203-1946 E. selkamarvenphoto@mailbox-demo.com

Colors
33b8a4
eea4c8
5c5c5c

Requirements
Must have
• I would like to include my logo on card.
Nice to have
• I also like the color brown as well as the choices below. I would like a simple, elegant card, something classy.

```html
<!DOCTYPE html>
<html lang="en">
<head>
<meta charset="utf-8">
<title>Selka Marven Photography – Business Card</title>
<link rel="stylesheet" href="https://fonts.googleapis.com/css2?family=Montserrat:wght@400;500;700&display=swap">
<style>
  :root {
    --bg: #e4e6ea;
    --brown-dark: #3d200f;
    --brown: #4e2b16;
    --brown-light: #6a4a32;
    --paper: #fbfbfb;
    --ink: #1c1c1c;
    --ink-soft: #4a4a4a;
    --cream: #f2e9e1;
    --pattern: rgba(190, 140, 110, 0.18);
  }
  * { box-sizing: border-box; margin: 0; padding: 0; }
  html, body { width: 1200px; height: 675px; overflow: hidden; }
  body {
    background: var(--bg);
    font-family: "Montserrat", Arial, sans-serif;
    position: relative;
  }
  .card {
    position: absolute;
    top: 189px;
    width: 520px;
    height: 297px;
    overflow: hidden;
    box-shadow: 0 6px 18px rgba(0,0,0,0.12);
  }

  /* Contact side */
  .card-back { left: 50px; background: var(--paper); }
  .brand-band {
    position: absolute; left: 0; top: 0; bottom: 0; width: 222px;
    background: linear-gradient(160deg, var(--brown-light) 0%, var(--brown) 45%, var(--brown-dark) 100%);
  }
  .band-notch {
    position: absolute; left: 222px; top: 100px;
    width: 0; height: 0;
    border-top: 10px solid transparent;
    border-bottom: 10px solid transparent;
    border-left: 10px solid var(--brown);
  }
  .band-pattern {
    position: absolute; left: 40px; top: -30px; width: 150px; height: 150px;
    border-radius: 50%;
    background: radial-gradient(circle, var(--pattern) 0%, rgba(190,140,110,0.06) 60%, transparent 72%);
  }
  .band-name {
    position: absolute; left: 0; width: 222px; top: 150px;
    text-align: center;
    color: var(--cream);
    font-size: 11px; font-weight: 500; letter-spacing: 1.5px;
    text-transform: uppercase; line-height: 1.5;
  }
  .city {
    position: absolute; left: 262px; top: 98px;
    font-size: 20px; font-weight: 700; letter-spacing: 4px;
    color: var(--ink); white-space: nowrap;
  }
  .city-marker {
    position: absolute; left: 476px; top: 90px;
    width: 0; height: 0;
    border-top: 8px solid transparent;
    border-bottom: 8px solid transparent;
    border-right: 12px solid var(--brown);
  }
  .contact-list {
    position: absolute; left: 262px; top: 166px;
    list-style: none;
  }
  .contact-item {
    display: flex; align-items: center; gap: 12px;
    height: 22px;
    font-size: 9.5px; letter-spacing: 0.5px; color: var(--ink-soft);
    white-space: nowrap;
  }
  .contact-icon { width: 12px; height: 12px; flex: none; }

  /* Brand side */
  .card-front {
    left: 630px;
    background: linear-gradient(200deg, var(--brown-light) 0%, var(--brown) 50%, var(--brown-dark) 100%);
  }
  .front-pattern {
    position: absolute; left: 10px; top: 50px; width: 240px; height: 210px;
    border-radius: 50%;
    background: radial-gradient(ellipse, var(--pattern) 0%, rgba(190,140,110,0.07) 55%, transparent 72%);
  }
  .front-name {
    position: absolute; left: 150px; top: 118px; width: 330px;
    text-align: center;
    color: var(--cream);
    font-size: 20px; font-weight: 500; letter-spacing: 3px;
    text-transform: uppercase; line-height: 1.45;
  }
  .front-web {
    position: absolute; right: 26px; bottom: 20px;
    font-size: 10px; letter-spacing: 1.5px; white-space: nowrap;
    color: rgba(200, 150, 120, 0.45);
  }
</style>
</head>
<body>

  <section class="card card-back" aria-label="Business card contact side">
    <div class="brand-band">
      <div class="band-pattern" role="img" aria-label="Faint interlocking octagon decoration"></div>
      <p class="band-name">Selka Marven<br>Photography</p>
    </div>
    <div class="band-notch"></div>
    <h2 class="city">GLENMOOR MA</h2>
    <div class="city-marker"></div>
    <ul class="contact-list">
      <li class="contact-item">
        <svg class="contact-icon" viewBox="0 0 12 12" aria-hidden="true"><rect x="2.5" y="0.5" width="7" height="11" rx="1" fill="none" stroke="#4a4a4a"/><line x1="5" y1="9.5" x2="7" y2="9.5" stroke="#4a4a4a"/></svg>
        <span>555-203-1946</span>
      </li>
      <li class="contact-item">
        <svg class="contact-icon" viewBox="0 0 12 12" aria-hidden="true"><rect x="0.5" y="2.5" width="11" height="7" fill="none" stroke="#4a4a4a"/><polyline points="0.5,2.5 6,6.5 11.5,2.5" fill="none" stroke="#4a4a4a"/></svg>
        <span>selkamarvenphoto@mailbox-demo.com</span>
      </li>
      <li class="contact-item">
        <svg class="contact-icon" viewBox="0 0 12 12" aria-hidden="true"><circle cx="6" cy="6" r="5.5" fill="none" stroke="#4a4a4a"/><ellipse cx="6" cy="6" rx="2.4" ry="5.5" fill="none" stroke="#4a4a4a"/><line x1="0.5" y1="6" x2="11.5" y2="6" stroke="#4a4a4a"/></svg>
        <span>www.selkamarvenphotography-demo.com</span>
      </li>
    </ul>
  </section>

  <section class="card card-front" aria-label="Business card brand side">
    <div class="front-pattern" role="img" aria-label="Faint interlocking octagon decoration"></div>
    <p class="front-name">Selka Marven<br>Photography</p>
    <p class="front-web">www.selkamarvenphotography-demo.com</p>
  </section>

</body>
</html>
```